stationary for hygienic company

We need a stationary design for hygienic company which provides public high end sanitary products and high end public lavatory.
We need a fresh and clean style stationary
we want the following things:
* logo (redesigned in eps/vector)
* Letterhead (with company details)
* letterhead (without company details)
* Business card
* note block
* ballpoint
* etcetera (a complete package)

```html
<!DOCTYPE html>
<html lang="fr">
<head>
<meta charset="utf-8">
<title>Velmira – Business cards</title>
<link rel="stylesheet" href="https://fonts.googleapis.com/css2?family=Roboto:wght@300;400;500&family=Roboto+Condensed:wght@300&display=swap">
<style>
  :root {
    --page: #ffffff;
    --page-edge: #d6d6d6;
    --navy: #00008a;
    --sky: #0096dc;
    --pink: #ff3399;
    --cyan: #00aaee;
    --violet: #5a5ab4;
    --ink-light: #ffffff;
    --ink-soft: #b8b8e6;
    --ink-soft-sky: #cfe9f8;
    --bar-grey: #b4b4b4;
    --bar-pale: #d2d2d2;
  }
  * { margin: 0; padding: 0; box-sizing: border-box; }
  html, body { width: 850px; height: 1200px; overflow: hidden; background: var(--page); }
  .sheet {
    position: relative; width: 850px; height: 1200px;
    border: 1px solid var(--page-edge);
    font-family: "Roboto", Arial, sans-serif;
  }
  .card {
    position: absolute; left: 243px; width: 364px; height: 203px;
    overflow: hidden; border: 1px solid #333;
  }
  .card--navy { background: var(--navy); }
  .card--sky { background: var(--sky); }
  .card--front-navy { top: 125px; }
  .card--back-navy { top: 361px; }
  .card--front-sky { top: 636px; }
  .card--back-sky { top: 872px; }

  .brand-field { position: absolute; right: 0; top: 0; width: 196px; height: 203px; }

  .holder { position: absolute; left: 29px; top: 66px; width: 130px; color: var(--ink-light); }
  .holder__name { font-size: 15px; font-weight: 500; letter-spacing: 0.2px; margin-bottom: 10px; white-space: nowrap; }
  .holder__line {
    font-family: "Roboto Condensed", "Arial Narrow", sans-serif;
    font-size: 9.6px; font-weight: 300; line-height: 13.8px;
    color: var(--ink-soft); white-space: nowrap;
  }
  .card--sky .holder__line { color: var(--ink-soft-sky); }

  .wordmark { color: var(--ink-light); font-weight: 400; text-align: center; line-height: 1; }
  .wordmark__name, .wordmark__tag, .wordmark__note { display: block; }

  .wordmark--corner { position: absolute; left: 246px; top: 28px; }
  .wordmark--corner .wordmark__name { font-size: 24px; letter-spacing: -0.5px; }
  .wordmark--corner .wordmark__tag { font-size: 8px; margin-top: 1px; }
  .wordmark--corner .wordmark__note { font-size: 4px; margin-top: 2px; }

  .wordmark--center { position: absolute; left: 0; right: 0; top: 36px; }
  .brand-dot {
    display: block; width: 34px; height: 34px; border-radius: 50%;
    margin: 0 auto 14px; background: var(--ink-light);
  }
  .wordmark--center .wordmark__name { font-size: 34px; letter-spacing: -0.8px; }
  .wordmark--center .wordmark__tag { font-size: 10px; margin-top: 2px; }
  .wordmark--center .wordmark__note { font-size: 4.5px; margin-top: 3px; }

  .stripe { position: absolute; left: 2px; top: 184px; width: 358px; height: 4px; display: flex; }
  .stripe span { height: 100%; }
  .stripe .seg-grey { width: 42px; background: var(--bar-grey); }
  .stripe .seg-pink { width: 19px; background: var(--pink); }
  .stripe .seg-gap { width: 9px; background: transparent; }
  .stripe .seg-navy { width: 9px; background: var(--navy); }
  .stripe .seg-blue { width: 60px; background: #1c6fd0; }
  .stripe .seg-violet { width: 60px; background: var(--violet); }
  .stripe .seg-pale { width: 74px; background: var(--bar-pale); }
  .stripe .seg-white { flex: 1; background: #ffffff; }
</style>
</head>
<body>
<main class="sheet">

  <section class="card card--navy card--front-navy">
    <svg class="brand-field" viewBox="0 0 196 203" role="img" aria-label="Brand graphic area in pink, violet and cyan">
      <defs>
        <linearGradient id="field-navy" x1="0" y1="0" x2="1" y2="1">
          <stop offset="0" stop-color="#ff3399"/>
          <stop offset="0.5" stop-color="#5a5ab4"/>
          <stop offset="1" stop-color="#00aaee"/>
        </linearGradient>
      </defs>
      <path d="M4 0 H196 V203 H44 C18 160 4 90 4 0 Z" fill="url(#field-navy)"/>
    </svg>
    <div class="holder">
      <p class="holder__name">Marc DELORME</p>
      <p class="holder__line">1842, Rue des Tilleuls nr. 12-14</p>
      <p class="holder__line">tel/fax: 0033 491 552170, 552171</p>
      <p class="holder__line">Marseille, code 130080, France</p>
      <p class="holder__line">www.velmira.fr, contact@velmira.fr</p>
    </div>
    <div class="wordmark wordmark--corner">
      <span class="wordmark__name">Velmira</span>
      <span class="wordmark__tag">Boutique Hygienique</span>
      <span class="wordmark__note">Marque déposée</span>
    </div>
  </section>

  <section class="card card--navy card--back-navy">
    <div class="wordmark wordmark--center">
      <span class="brand-dot"></span>
      <span class="wordmark__name">Velmira</span>
      <span class="wordmark__tag">Boutique Hygienique</span>
      <span class="wordmark__note">Marque déposée</span>
    </div>
    <div class="stripe">
      <span class="seg-grey"></span><span class="seg-pink"></span><span class="seg-gap"></span>
      <span class="seg-blue"></span><span class="seg-pale"></span><span class="seg-white"></span>
    </div>
  </section>

  <section class="card card--sky card--front-sky">
    <svg class="brand-field" viewBox="0 0 196 203" role="img" aria-label="Brand graphic area in pink, navy and cyan">
      <defs>
        <linearGradient id="field-sky" x1="0" y1="0" x2="1" y2="1">
          <stop offset="0" stop-color="#ff3399"/>
          <stop offset="0.5" stop-color="#1a1a9a"/>
          <stop offset="1" stop-color="#00aaee"/>
        </linearGradient>
      </defs>
      <path d="M4 0 H196 V203 H44 C18 160 4 90 4 0 Z" fill="url(#field-sky)"/>
    </svg>
    <div class="holder">
      <p class="holder__name">Marc DELORME</p>
      <p class="holder__line">1842, Rue des Tilleuls nr. 12-14</p>
      <p class="holder__line">tel/fax: 0033 491 552170, 552171</p>
      <p class="holder__line">Marseille, code 130080, France</p>
      <p class="holder__line">www.velmira.fr, contact@velmira.fr</p>
    </div>
    <div class="wordmark wordmark--corner">
      <span class="wordmark__name">Velmira</span>
      <span class="wordmark__tag">Boutique Hygienique</span>
      <span class="wordmark__note">Marque déposée</span>
    </div>
  </section>

  <section class="card card--sky card--back-sky">
    <div class="wordmark wordmark--center">
      <span class="brand-dot"></span>
      <span class="wordmark__name">Velmira</span>
      <span class="wordmark__tag">Boutique Hygienique</span>
      <span class="wordmark__note">Marque déposée</span>
    </div>
    <div class="stripe">
      <span class="seg-grey"></span><span class="seg-pink"></span><span class="seg-navy"></span>
      <span class="seg-violet"></span><span class="seg-pale"></span><span class="seg-white"></span>
    </div>
  </section>

</main>
</body>
</html>
```